Business Card needed for Drainor, a growing Septic Service company

Drainor, a growing local septic service company in Pennsylvania, needs updated business cards. We'd like the business card to feature our logo and communicate that we provide Septic Pumping, Installations/Repairs, Restroom Rentals, and 24/7 Emergency Service. The business card should be eye-catching, bold, and clean/simple. We have been in business almost 10 years and would like to expand and update our business brand and image.

Target Market(s)

Residential and Commercial, New and Current Homeowners

Industry/Entity Type

Service

Contact Information for Business Card

Contact on the business card should be: Dean Harlow Owner & Operator
Phone: 610-555-0187
Email: service@drainor-example.com
Website: www.drainor-example.com
Address: 812 Millbrook Lane Easton PA 18042

Font styles to use
Sans Serif

Colors

Designer to choose colors to be used in the design.

Requirements
Must have
• Feature logo on both side of business card.
Nice to have
• We envision the contact information on one side and our services listed on the other side. Utilize the green from the symbol in our logo as part of the design, overall design color scheme should be white, grey, black.

```html
<!DOCTYPE html>
<html lang="en">
<head>
<meta charset="utf-8">
<title>Drainor Business Card</title>
<link href="https://fonts.googleapis.com/css2?family=Open+Sans:wght@400;600;700&display=swap" rel="stylesheet">
<style>
  :root {
    --brand-green: #82bc3f;
    --card-white: #f4f4f4;
    --ink: #1a1a1a;
    --backdrop: #e2e2e2;
    --text-light: #ffffff;
  }
  * { margin: 0; padding: 0; box-sizing: border-box; }
  html, body {
    width: 1200px; height: 960px; overflow: hidden;
    background: var(--backdrop);
    font-family: "Open Sans", Arial, sans-serif;
  }
  .canvas { position: relative; width: 1200px; height: 960px; }
  .card {
    position: absolute; left: 306px; width: 585px; height: 334px;
  }
  .card--front { top: 121px; background: var(--brand-green); color: var(--text-light); }
  .card--back { top: 506px; background: var(--card-white); color: var(--ink); }

  .front-brand {
    position: absolute; left: 0; right: 0; top: 250px; transform: translateY(-150px);
    display: flex; align-items: center; justify-content: center; gap: 14px;
  }
  .front-brand__square { width: 36px; height: 36px; background: var(--text-light); }
  .front-brand__name { font-size: 46px; font-weight: 700; color: var(--text-light); line-height: 1; }

  .services {
    position: absolute; left: 0; right: 0; top: 266px;
    text-align: center; font-size: 16px; font-weight: 400;
    display: flex; justify-content: center; align-items: center; gap: 6px;
  }
  .services__dot { width: 7px; height: 7px; border-radius: 50%; background: var(--text-light); display: inline-block; }
  .emergency {
    position: absolute; left: 0; right: 0; top: 291px;
    text-align: center; font-size: 16px; font-weight: 700; letter-spacing: 0.2px;
  }

  .back-brand {
    position: absolute; left: 58px; top: 149px;
    display: flex; align-items: center; gap: 10px;
  }
  .back-brand__square { width: 34px; height: 34px; background: var(--brand-green); }
  .back-brand__name { font-size: 34px; font-weight: 700; color: var(--ink); line-height: 1; }

  .divider {
    position: absolute; left: 292px; top: 107px; width: 1.5px; height: 122px;
    background: var(--brand-green);
  }
  .contact { position: absolute; left: 334px; top: 106px; }
  .contact__name { color: var(--brand-green); font-size: 20px; font-weight: 700; line-height: 24px; }
  .contact__role { font-size: 16px; line-height: 22px; }
  .contact__list { list-style: none; margin-top: 16px; }
  .contact__item { display: flex; align-items: center; gap: 7px; font-size: 16px; line-height: 20px; }
  .contact__icon { width: 12px; height: 12px; flex: none; }

  .address {
    position: absolute; left: 0; right: 0; top: 285px;
    text-align: center; font-size: 15px;
  }
</style>
</head>
<body>
<main class="canvas">
  <section class="card card--front" aria-label="Card front">
    <div class="front-brand">
      <span class="front-brand__square"></span>
      <span class="front-brand__name">Drainor</span>
    </div>
    <p class="services">
      <span>Septic Pumping</span><span class="services__dot"></span>
      <span>Installations/Repairs</span><span class="services__dot"></span>
      <span>Restroom Rentals</span>
    </p>
    <p class="emergency">24/7 EMERGENCY SERVICE</p>
  </section>

  <section class="card card--back" aria-label="Card back">
    <div class="back-brand">
      <span class="back-brand__square"></span>
      <span class="back-brand__name">Drainor</span>
    </div>
    <div class="divider"></div>
    <div class="contact">
      <p class="contact__name">DEAN HARLOW</p>
      <p class="contact__role">Owner &amp; Operator</p>
      <ul class="contact__list">
        <li class="contact__item">
          <svg class="contact__icon" viewBox="0 0 24 24" aria-hidden="true"><path fill="#82bc3f" d="M6.6 10.8a15.1 15.1 0 0 0 6.6 6.6l2.2-2.2c.3-.3.7-.4 1-.2 1.1.4 2.3.6 3.6.6.6 0 1 .4 1 1V20c0 .6-.4 1-1 1A17 17 0 0 1 3 4c0-.6.4-1 1-1h3.5c.6 0 1 .4 1 1 0 1.3.2 2.5.6 3.6.1.3 0 .7-.2 1z"/></svg>
          <span>610-555-0187</span>
        </li>
        <li class="contact__item">
          <svg class="contact__icon" viewBox="0 0 24 24" aria-hidden="true"><rect x="2" y="5" width="20" height="14" fill="none" stroke="#82bc3f" stroke-width="2.4"/><path d="M2 5l10 8 10-8" fill="none" stroke="#82bc3f" stroke-width="2.4"/></svg>
          <span>service@drainor-example.com</span>
        </li>
        <li class="contact__item">
          <svg class="contact__icon" viewBox="0 0 24 24" aria-hidden="true"><g fill="none" stroke="#82bc3f" stroke-width="2"><circle cx="12" cy="12" r="10"/><ellipse cx="12" cy="12" rx="4.5" ry="10"/><path d="M2 12h20M4 7h16M4 17h16"/></g></svg>
          <span>www.drainor-example.com</span>
        </li>
      </ul>
    </div>
    <p class="address">812 Millbrook Lane Easton PA 18042</p>
  </section>
</main>
</body>
</html>
```